Elegant brochure design for startup

We want to design an advertising booklet to introduce our company as a professional and trustworthy.

please take a look at the attached content templet to read know more about our business and services. Also to see what each page of the booklet should contain.

The size of the booklet should be around the half of A4 page. 12 pages includes the cover and back page ( See content templet attached )

We will provide content, pictures, and logo and our specifications for the
designer

Target Market(s)

We want to target executives in private and government sectors, the decision makers who are open to new and fresh ideas

Industry/Entity Type

Business Consultant

Font styles to use
Sans Serif

Requirements
Must have
• - Attractive, elegant, eyes catching design inspired attached identity.
• - bright color background for the writhing to make it easier for readers
• - neat arrangement of the content throughout the booklet. For example, arranging the content in a boxes using colors etc. to make easier for the reader.
Nice to have
• - icons to explane some of the content.
• - Info-graphic style when it make the content (in some parts easer to read )
• - Simple and elegant
• - We have a simi human icon as the letter "i" in our logo .. you may use it in some forms to represent human icon. Also you can modify it to represent deferent human format (Doctors - women - factory employee etc.
Should not have
• - don't use human pictures ! we prefer to use graphic abstract shapes and colors.
• - We don't prefer crowded pages ..
• - Our work is all about LOCAL organizational culture and employees. We are taking about the local market and as you know our local uniform is deferent than the western dress uniform. That's way we don't want to put a pic with a man in suit or women in short uniform. You can use icon like the ones when you search ( saudi employee icon) (without showing the faces - shadow format)

```html
<!DOCTYPE html>
<html lang="en">
<head>
<meta charset="utf-8">
<title>Brightfield – Booklet Spreads</title>
<link rel="stylesheet" href="https://fonts.googleapis.com/css2?family=Quicksand:wght@400;500;600;700&display=swap">
<style>
  :root{
    --stage:#d1d2d4;
    --navy:#0f4a80;
    --navy-deep:#0b3d6e;
    --sky:#00aeef;
    --white:#ffffff;
    --ink:#1d3f66;
  }
  *{box-sizing:border-box;margin:0;padding:0}
  html,body{width:1200px;height:1200px;overflow:hidden}
  body{background:var(--stage);font-family:"Quicksand",sans-serif;color:var(--white);position:relative}
  .spread{position:absolute;overflow:hidden}
  .abs{position:absolute}

  .brand{font-weight:600;line-height:1;letter-spacing:.3px;color:var(--white);white-space:nowrap}
  .brand.on-light{color:var(--navy)}
  .motto{font-size:10px;letter-spacing:.5px;margin-top:8px;font-weight:500;white-space:nowrap}

  /* spread 1: covers */
  .covers{left:86px;top:76px;width:1020px;height:330px;
    background:radial-gradient(ellipse at 72% 55%,#1a5a96 0%,var(--navy) 45%,var(--navy-deep) 100%)}
  .covers .fold{left:510px;top:0;width:1px;height:100%;background:rgba(255,255,255,.18)}
  .back-brand{left:61px;top:160px}
  .back-brand .brand{font-size:30px}
  .contact{left:246px;top:148px;font-size:11px;line-height:16.7px;font-weight:500}
  .contact li{list-style:none;display:flex;gap:10px}
  .contact .ico{width:11px;flex:none;display:flex;align-items:center;justify-content:center;color:var(--sky)}
  .contact .ico svg{width:9px;height:9px}
  .socials{left:78px;top:275px;display:flex;gap:4px}
  .socials span{width:18px;height:18px;background:var(--white)}
  .back-url{left:244px;top:279px;font-size:11px;letter-spacing:.8px}
  .front-brand{left:676px;top:150px}
  .front-brand .brand{font-size:44px}
  .front-brand .motto{font-size:13px;margin-top:12px;letter-spacing:1px}
  .front-url{left:674px;top:283px;font-size:11px;letter-spacing:.8px}

  /* spread 2: values + about */
  .values{left:90px;top:436px;width:1021px;height:330px;background:var(--white)}
  .values .pillars{left:0;top:0;width:511px;height:330px;
    background:linear-gradient(125deg,#07a7e6 0%,var(--sky) 50%,#22b8f0 100%)}
  .pillar-dot{width:52px;height:52px;border-radius:50%;background:var(--white);
    box-shadow:0 3px 4px rgba(0,0,0,.18);display:flex;align-items:center;justify-content:center}
  .pillar-dot svg{width:28px;height:28px}
  .pillar-text{width:250px;font-size:12.5px;line-height:16px}
  .pillar-text b{color:var(--navy);font-weight:700}
  .about-bg{left:511px;top:0;width:510px;height:330px;
    background:linear-gradient(200deg,#d6e6f5 0%,#f3f8fc 35%,var(--white) 60%)}
  .about-brand{left:546px;top:44px}
  .about-brand .brand{font-size:27px}
  .about-brand .motto{font-size:8px;color:var(--navy);margin-top:6px}
  .about-copy{left:546px;top:119px;width:450px;font-size:10.5px;line-height:14px;color:var(--ink)}
  .about-copy b{color:var(--navy);font-size:13px;font-weight:700}
  .promise-box{left:533px;top:220px;width:467px;height:92px;border-radius:6px;background:var(--navy);
    padding:10px 28px;font-size:10.5px;line-height:14px}

  /* spread 3: services + mission */
  .services{left:90px;top:800px;width:1021px;height:330px;background:var(--white)}
  .svc-core{left:36px;top:47px;width:215px;font-size:13px;line-height:16px;color:var(--ink)}
  .svc-core b{color:var(--navy);font-weight:700}
  .svc-list{list-style:none;font-size:13px;line-height:16px}
  .svc-list li{display:flex;gap:14px;margin-bottom:4px}
  .svc-list svg{width:14px;height:14px;flex:none;margin-top:1px}
  .core-list{left:42px;top:198px;color:var(--ink)}
  .core-list svg{color:var(--navy)}
  .svc-extra{left:269px;top:0;width:242px;height:330px;background:var(--sky)}
  .extra-copy{left:294px;top:52px;width:198px;font-size:13px;line-height:16px}
  .extra-list{left:294px;top:164px}
  .extra-list li{margin-bottom:0}
  .extra-list span{width:150px}
  .mission-panel{left:511px;top:0;width:510px;height:330px;background:var(--navy)}
  .mission-brand{left:555px;top:36px}
  .mission-brand .brand{font-size:27px}
  .mission-brand .motto{font-size:8px;margin-top:6px}
  .mission-box{left:546px;top:103px;width:222px;height:212px;border-radius:5px;
    background:linear-gradient(180deg,var(--white) 0%,#e9f1fa 70%,#bcd3ec 100%);
    padding:21px 12px 0 14px;color:var(--ink);font-size:10.5px;line-height:13.6px}
  .mission-box h3{font-size:13px;font-weight:700;color:var(--navy);line-height:14px}
  .mission-box p+p{margin-top:13px}
  .mission-badge{left:698px;top:76px;width:52px;height:52px;border-radius:50%;background:var(--sky);
    box-shadow:0 3px 4px rgba(0,0,0,.25);display:flex;align-items:center;justify-content:center}
  .social-duty{left:824px;top:158px;width:150px;font-size:10.5px;line-height:14px}
  .social-duty h3{font-size:13px;font-weight:700;line-height:16px}
</style>
</head>
<body>

<section class="spread covers" aria-label="Back and front cover">
  <div class="abs fold"></div>

  <div class="abs back-brand">
    <div class="brand">Brightfield</div>
    <div class="motto">people · culture · growth</div>
  </div>

  <ul class="abs contact">
    <li><span class="ico"><svg viewBox="0 0 10 10"><path d="M5 1 L9.5 5 H8 V9 H2 V5 H.5Z" fill="currentColor"/></svg></span>Al-Waha Tower, Palm Garden St.</li>
    <li><span class="ico"></span>Suite 410 Jeddah, Makkah 21400</li>
    <li><span class="ico"></span>Saudi Arabia</li>
    <li><span class="ico"><svg viewBox="0 0 10 10"><path d="M2 1 L4 3 L3 4.5 Q4.5 6.5 5.5 7 L7 6 L9 8 L7.5 9.5 Q2 8 .5 2.5Z" fill="currentColor"/></svg></span>Tel: +966125550142</li>
    <li><span class="ico"><svg viewBox="0 0 10 10"><rect x="2.5" y=".5" width="5" height="9" rx="1" fill="currentColor"/></svg></span>Mobile: +966505550178</li>
    <li><span class="ico"><svg viewBox="0 0 10 10"><rect x=".5" y="2" width="9" height="6" fill="currentColor"/><path d="M.5 2 L5 5.5 L9.5 2" stroke="#0f4a80" fill="none"/></svg></span>Email: info@brightfield.example</li>
  </ul>

  <div class="abs socials" aria-label="Social profiles"><span></span><span></span><span></span><span></span></div>
  <div class="abs back-url">www.brightfield.example</div>

  <div class="abs front-brand">
    <div class="brand">Brightfield</div>
    <div class="motto">people · culture · growth</div>
  </div>
  <div class="abs front-url">www.brightfield.example</div>
</section>

<section class="spread values" aria-label="Values and about spread">
  <div class="abs pillars"></div>

  <div class="abs pillar-dot" style="left:89px;top:40px">
    <svg viewBox="0 0 28 28"><path d="M14 4 L22 13 H17 V24 H11 V13 H6Z" fill="#0f4a80"/></svg>
  </div>
  <p class="abs pillar-text" style="left:158px;top:50px"><b>ATTRACT</b> the top talent available in the workforce market by optimizing their workplace to become a workplace of choice;</p>

  <div class="abs pillar-dot" style="left:89px;top:149px">
    <svg viewBox="0 0 28 28"><rect x="4" y="16" width="5" height="8" fill="#0f4a80"/><rect x="11.5" y="11" width="5" height="13" fill="#0f4a80"/><rect x="19" y="6" width="5" height="18" fill="#0f4a80"/><rect x="3" y="24" width="22" height="1.5" fill="#0f4a80"/></svg>
  </div>
  <p class="abs pillar-text" style="left:158px;top:162px"><b>ENGAGE</b> human capital to the best of their abilities and increase performance and productivity; and</p>

  <div class="abs pillar-dot" style="left:89px;top:238px">
    <svg viewBox="0 0 28 28"><circle cx="14" cy="14" r="10" fill="none" stroke="#0f4a80" stroke-width="2.5"/><circle cx="14" cy="14" r="4" fill="#0f4a80"/></svg>
  </div>
  <p class="abs pillar-text" style="left:158px;top:258px"><b>RETAIN</b> the top talent by connecting them mentally and emotionally to their workplace.</p>

  <div class="abs about-bg"></div>
  <div class="abs about-brand">
    <div class="brand on-light">Brightfield</div>
    <div class="motto">people · culture · growth</div>
  </div>
  <p class="abs about-copy"><b>BRIGHTFIELD</b> is a team of employee-engagement, internal communication, and organizational culture experts with both local and international backgrounds. With our expertise and longstanding experience, we can help organizations like yours to diagnose problems optimally, to measure your employee-engagement level, and to handle workplace-related challenges in organizational culture and internal communications.</p>
  <div class="abs promise-box">We know the right practices and the path that leads to business success and high employee-engagement rates. We are willing to work side by side with you to help you achieve your goals, attract and engage the right candidates, align them with your organization’s values and objectives, and create the best organizational culture to guarantee high retention rates.</div>
</section>

<section class="spread services" aria-label="Services and mission spread">
  <p class="abs svc-core"><b>BRIGHTFIELD</b> provides professional business services focusing mainly on improving the workplace environment and increasing the level of employee engagement by using best practice from various related areas, such as</p>
  <ul class="abs svc-list core-list">
    <li><svg viewBox="0 0 14 14"><rect x="2.5" y="1" width="9" height="12" fill="none" stroke="currentColor" stroke-width="1.4"/><path d="M4.5 5h5M4.5 7.5h5M4.5 10h5" stroke="currentColor"/></svg><span>Employee-Engagement<br>Surveys</span></li>
    <li><svg viewBox="0 0 14 14"><ellipse cx="7" cy="6" rx="6" ry="4" fill="currentColor"/><path d="M3 9 L2 13 L6 10Z" fill="currentColor"/></svg><span>Internal Communications</span></li>
    <li><svg viewBox="0 0 14 14"><circle cx="7" cy="6" r="4.5" fill="currentColor"/><path d="M1 9 L7 13 L13 9" stroke="currentColor" stroke-width="1.5" fill="none"/></svg><span>Organizational Culture</span></li>
    <li><svg viewBox="0 0 14 14"><circle cx="7" cy="7" r="5.5" fill="none" stroke="currentColor" stroke-width="1.4"/><circle cx="7" cy="7" r="2.5" fill="currentColor"/></svg><span>Recognition and Reward</span></li>
  </ul>

  <div class="abs svc-extra"></div>
  <p class="abs extra-copy">In addition, our services include business process outsourcing of various business functionalities to help companies focus on their core business. These services include</p>
  <ul class="abs svc-list extra-list">
    <li><svg viewBox="0 0 14 14"><circle cx="7" cy="7" r="3" fill="#fff"/><circle cx="7" cy="7" r="6" fill="none" stroke="#fff" stroke-dasharray="2 2"/></svg><span>Human Resources Outsourcing</span></li>
    <li><svg viewBox="0 0 14 14"><rect x="6" y="2" width="7" height="6" fill="none" stroke="#fff" stroke-width="1.3"/><rect x="1" y="6" width="3" height="7" fill="#fff"/></svg><span>Specialized Training and Coaching</span></li>
    <li><svg viewBox="0 0 14 14"><rect x="4" y="5" width="6" height="4" fill="#fff"/><path d="M1 4v6M13 4v6" stroke="#fff" stroke-width="1.5"/></svg><span>Back- and Front-Office Outsourcing</span></li>
    <li><svg viewBox="0 0 14 14"><rect x="1" y="2" width="6" height="7" fill="#fff"/><rect x="9" y="5" width="3" height="8" fill="#fff"/></svg><span>Customer Experience Auditing</span></li>
  </ul>

  <div class="abs mission-panel"></div>
  <div class="abs mission-brand">
    <div class="brand">Brightfield</div>
    <div class="motto">people · culture · growth</div>
  </div>
  <div class="abs mission-box">
    <h3>OUR MISSION</h3>
    <p>Our mission is to enable an organization’s human capital to play the biggest possible role in its success.</p>
    <p>We are dedicated to helping organizations become more successful through their human capital and by implementing the methods and strategies to make that human capital play the most significant role in the organization’s success.</p>
  </div>
  <div class="abs mission-badge">
    <svg viewBox="0 0 28 28" width="28" height="28"><circle cx="13" cy="15" r="9" fill="none" stroke="#fff" stroke-width="2"/><circle cx="13" cy="15" r="5" fill="none" stroke="#fff" stroke-width="2"/><circle cx="13" cy="15" r="1.8" fill="#fff"/><path d="M13 15 L23 5 M20 4 L23 5 L24 8" stroke="#fff" stroke-width="2" fill="none"/></svg>
  </div>
  <div class="abs social-duty">
    <h3>Our Social<br>Responsibility</h3>
    <p>We aspire to contribute to the national strategy aimed at reducing the unemployment rate by helping organizations to add sustainable, high-quality jobs to the Saudi market.</p>
  </div>
</section>

</body>
</html>
```